MARLOWE THREADWORK WEB DESIGN PROJECT

We are a brand new company called "Marlowe Threadwork" which specialise in one-off Vintage Clothing. We would like somebody to design a web page which will be the sole income for our company. Our main aim is to have an easy searchable website which is user friendly. The key to the website is to target people who do not like the idea of op-shopping but love vintage clothes - this website will be the answer.
Updates

This website will need to be coded to work with Halvo Shopdesk - Please read this before you start. https://help.halvoshopdesk.example/articles/Public/How-do-I-create-custom-template-files-for-my-store

Hi everyone, Just want to make note that the this website is for young people. Just so people a clear I want modern young people dressed in Vintage clothes as this is that reality and what they would like to see. Not people dressed like they are going to a fancy dress party, i.e. dresses like it was that era. Thanks Rosalind

Coding

Coded - Design and coding required

```html
<!DOCTYPE html>
<html lang="en">
<head>
<meta charset="utf-8">
<title>Marlowe Threadwork — Unique Vintage Fashion and Accessories</title>
<link href="https://fonts.googleapis.com/css2?family=Open+Sans:wdth,wght@75..100,300..700&display=swap" rel="stylesheet">
<style>
  :root {
    --teal: #48b8c6;
    --teal-ink: #1f5a63;
    --white: #ffffff;
    --ink: #111111;
    --pill: #2b2b2b;
    --pink: #d9449a;
    --rule: #dadada;
    --accent: #b9412b;
    --muted: #9a9a9a;
  }
  * { box-sizing: border-box; margin: 0; padding: 0; }
  html, body { width: 1200px; height: 900px; overflow: hidden; background: var(--white); }
  body { position: relative; font-family: "Open Sans", Arial, sans-serif; color: var(--ink); }

  .utility-bar { position: absolute; top: 0; right: 76px; height: 21px; display: flex; align-items: center; gap: 8px; font-size: 11px; letter-spacing: .5px; color: var(--teal); }
  .utility-bar .social { display: inline-block; width: 7px; height: 9px; background: var(--teal); margin-left: 3px; }

  .site-header { position: absolute; top: 21px; left: 0; width: 1200px; height: 122px; background: var(--teal); }
  .brand-name { position: absolute; left: 78px; top: 22px; font-size: 34px; font-weight: 400; color: var(--white); white-space: nowrap; }
  .brand-tagline { position: absolute; left: 78px; top: 80px; font-size: 22px; font-weight: 300; font-stretch: 75%; color: var(--teal-ink); letter-spacing: .1px; white-space: nowrap; }
  .account-button { position: absolute; top: 28px; height: 30px; border: 1.5px solid var(--white); border-radius: 8px; color: var(--white); font-size: 15px; font-weight: 300; display: flex; align-items: center; justify-content: center; }
  .account-button.login { left: 942px; width: 88px; }
  .account-button.signup { left: 1039px; width: 88px; }
  .search-box { position: absolute; left: 940px; top: 78px; width: 188px; height: 38px; background: var(--white); font-size: 13px; font-weight: 300; color: var(--muted); padding: 13px 0 0 9px; white-space: nowrap; }
  .search-box svg { position: absolute; right: 6px; top: 12px; }

  .main-nav { position: absolute; top: 166px; left: 62px; display: flex; align-items: center; height: 34px; font-size: 19px; white-space: nowrap; }
  .main-nav .sep { margin: 0 12px; }
  .main-nav .home { margin-right: 9px; }
  .style-tips { margin-left: 10px; background: var(--pill); color: var(--white); border-radius: 50%; width: 132px; height: 34px; display: flex; align-items: center; justify-content: center; font-size: 17px; }
  .shipping-note { position: absolute; top: 167px; right: 75px; font-size: 19px; letter-spacing: .3px; white-space: nowrap; }

  .hero { position: absolute; left: 61px; top: 209px; width: 1069px; height: 405px; background: linear-gradient(180deg, #ecd8bd 0%, #ead2b0 70%, #d9b68c 88%, #e7cdb0 100%); }
  .hero-title { position: absolute; left: 374px; width: 650px; top: 134px; text-align: center; color: var(--pink); font-size: 44px; line-height: 1.1; font-weight: 700; letter-spacing: -2px; white-space: nowrap; }
  .hero-subtitle { position: absolute; left: 374px; width: 650px; top: 205px; text-align: center; font-size: 44px; line-height: 1.1; font-weight: 300; font-stretch: 75%; white-space: nowrap; }
  .join-button { position: absolute; left: 561px; top: 277px; width: 267px; height: 66px; border: 2px solid var(--ink); border-radius: 8px; display: flex; align-items: center; justify-content: center; font-size: 21px; font-weight: 300; font-stretch: 85%; }
  .hero-arrow { position: absolute; width: 42px; height: 42px; background: rgba(255,255,255,.45); color: #b8b8b8; font-size: 36px; font-weight: 300; display: flex; align-items: center; justify-content: center; }
  .hero-arrow.prev { left: 0; top: 162px; }
  .hero-arrow.next { right: 0; top: 168px; }

  .divider { position: absolute; left: 61px; top: 624px; width: 1068px; height: 9px; background: var(--rule); }
  .section-title { position: absolute; left: 62px; top: 649px; font-size: 27px; line-height: 1.3; font-weight: 400; color: var(--accent); }
  .pick { position: absolute; top: 706px; width: 243px; height: 194px; }
  .pick.one { left: 61px; background: linear-gradient(180deg, #4a6a8c 0%, #5a4a44 60%, #2c2a30 100%); }
  .pick.two { left: 335px; background: linear-gradient(180deg, #c8dbe9 0%, #b6cadb 60%, #9aa6ae 100%); }
  .pick.three { left: 611px; background: linear-gradient(160deg, #e9c08a 0%, #b76a3a 50%, #4a2a1c 100%); }
  .pick.four { left: 888px; background: linear-gradient(180deg, #2d3324 0%, #b9b6a8 45%, #55513a 100%); }
</style>
</head>
<body>
  <div class="utility-bar">
    <span>VIEW CART</span><span>|</span><span>WISH LIST</span>
    <span class="social"></span><span class="social"></span><span class="social"></span>
  </div>

  <header class="site-header">
    <div class="brand-name">Marlowe Threadwork</div>
    <div class="brand-tagline">UNIQUE VINTAGE FASHION AND ACCESSORIES</div>
    <div class="account-button login">LOG IN</div>
    <div class="account-button signup">SIGN UP</div>
    <div class="search-box">Search for unique pieces
      <svg width="16" height="16" viewBox="0 0 16 16"><circle cx="6.5" cy="6.5" r="5" fill="none" stroke="#bbbbbb" stroke-width="1.8"/><line x1="10.2" y1="10.2" x2="15" y2="15" stroke="#bbbbbb" stroke-width="2"/></svg>
    </div>
  </header>

  <nav class="main-nav">
    <svg class="home" width="30" height="26" viewBox="0 0 30 26"><path d="M15 1 L1 13 L4 13 L4 25 L12 25 L12 17 L18 17 L18 25 L26 25 L26 13 L29 13 Z" fill="#222"/></svg>
    <span>WOMEN</span><span class="sep">|</span><span>MEN</span><span class="sep">|</span><span>FAQs</span>
    <span class="style-tips">STYLE TIPS</span>
  </nav>
  <div class="shipping-note">FREE SHIPPING FOR ORDERS OVER $100</div>

  <section class="hero" role="img" aria-label="Photo of a young woman in a straw hat and floral vintage dress on a sunlit beach">
    <div class="hero-title">Lorem ipsum dolor set amet</div>
    <div class="hero-subtitle">A NEW WAY TO OP SHOP.</div>
    <div class="join-button">JOIN US</div>
    <div class="hero-arrow prev">&lt;</div>
    <div class="hero-arrow next">&gt;</div>
  </section>

  <div class="divider"></div>
  <h2 class="section-title">Top picks</h2>
  <div class="pick one" role="img" aria-label="Woman with a long braid in a dark jacket, seen from behind"></div>
  <div class="pick two" role="img" aria-label="Legs in grey jeans against a pale sky"></div>
  <div class="pick three" role="img" aria-label="Woman in a checked shirt in warm sunset light, seen from behind"></div>
  <div class="pick four" role="img" aria-label="White lace dress in a forest"></div>
</body>
</html>
```